IT Consulting, IT Guru, Software Development, Network Solutions, Hosting

Attached is logo for our company, we just was the designers to come up with creative ideas to use the logo and the theme to come with creative and energetic business cards that leave an impression and stick in people's head.

Target Market(s)

Medical, Law, Entertainment, Real estate, any small to medium size business.

Industry/Entity Type

Business

Font styles to use
Serif
Sans Serif

```html
<!DOCTYPE html>
<html lang="en">
<head>
<meta charset="utf-8">
<title>Voltrix Business Card</title>
<link rel="stylesheet" href="https://fonts.googleapis.com/css2?family=Didact+Gothic&family=Merriweather:ital,wght@1,900&family=Arimo:wght@700&display=swap">
<style>
  :root {
    --page: #ffffff;
    --card: #1f2326;
    --card-deep: #15181a;
    --ink: #f2f2f2;
    --gold: #e8c21c;
    --silver: #9aa0a4;
    --silver-soft: #5d6367;
    --glow: rgba(255, 255, 255, 0.55);
  }
  * { margin: 0; padding: 0; box-sizing: border-box; }
  html, body {
    width: 938px;
    height: 1200px;
    overflow: hidden;
    background: var(--page);
  }
  .sheet {
    position: relative;
    width: 938px;
    height: 1200px;
  }
  .card {
    position: absolute;
    left: 79px;
    width: 780px;
    height: 462px;
    overflow: hidden;
    background: linear-gradient(180deg, var(--card) 0%, var(--card-deep) 100%);
  }
  .card--front { top: 110px; }
  .card--back { top: 628px; }

  /* front */
  .front-ornament {
    position: absolute;
    left: 50px;
    top: 130px;
    width: 680px;
    height: 210px;
    border-radius: 105px;
    background: radial-gradient(ellipse at center, rgba(154,160,164,0.45) 0%, rgba(93,99,103,0.35) 45%, rgba(31,35,38,0) 75%);
  }
  .front-disc {
    position: absolute;
    left: 268px;
    top: 108px;
    width: 244px;
    height: 244px;
    border-radius: 50%;
    background: radial-gradient(circle at 50% 45%, #25292c 0%, #121416 100%);
    box-shadow: 0 0 26px 10px var(--glow), 0 0 60px 20px rgba(255,255,255,0.18);
  }
  .brand-name {
    font-family: "Didact Gothic", "Century Gothic", sans-serif;
    font-weight: 400;
    color: var(--gold);
    letter-spacing: 1px;
    white-space: nowrap;
  }
  .front-disc .brand-name {
    position: absolute;
    left: 0;
    right: 0;
    top: 100px;
    text-align: center;
    font-size: 38px;
  }

  /* back */
  .back-brand {
    position: absolute;
    left: 68px;
    top: 72px;
  }
  .back-brand .brand-name { font-size: 44px; display: block; }
  .tagline {
    display: block;
    margin-top: 4px;
    font-family: "Merriweather", Georgia, serif;
    font-style: italic;
    font-weight: 900;
    font-size: 21px;
    color: var(--ink);
  }
  .contact {
    position: absolute;
    left: 24px;
    top: 308px;
    font-family: "Arimo", Arial, sans-serif;
    font-weight: 700;
    font-size: 14px;
    line-height: 19px;
    color: var(--ink);
    list-style: none;
  }
  .contact .gap { height: 12px; }
  .back-ornament {
    position: absolute;
    right: -20px;
    bottom: -20px;
    width: 400px;
    height: 330px;
    border-top-left-radius: 260px 220px;
    background:
      radial-gradient(ellipse at 75% 70%, rgba(232,194,28,0.35) 0%, rgba(232,194,28,0) 45%),
      radial-gradient(ellipse at 60% 60%, rgba(154,160,164,0.55) 0%, rgba(93,99,103,0.3) 50%, rgba(31,35,38,0) 80%);
  }
</style>
</head>
<body>
  <main class="sheet">
    <section class="card card--front" aria-label="Card front">
      <div class="front-ornament" role="img" aria-label="Silver swirl ornament spreading left and right behind the central disc"></div>
      <div class="front-disc">
        <span class="brand-name">VOLTRIX</span>
      </div>
    </section>

    <section class="card card--back" aria-label="Card back">
      <div class="back-ornament" role="img" aria-label="Silver and gold swirl ornament in the lower right corner"></div>
      <div class="back-brand">
        <span class="brand-name">VOLTRIX</span>
        <span class="tagline">smal description text</span>
      </div>
      <ul class="contact">
        <li>Telephone: 000.00.00.00.00</li>
        <li>Hemsidan: www.yourwebsite.dmn</li>
        <li>Email: youremail@mail.dmn</li>
        <li class="gap"></li>
        <li>Adress:</li>
        <li>yoor Business Adress;</li>
      </ul>
    </section>
  </main>
</body>
</html>
```